Poster for a online company that buys your stuff

SwapHollow offers a website which customers can get a instant offer for stuff their looking to sell. They then Courier the items in to us and they get paid the same day it arrives
We're looking for an eye catching design which portrays our hassle free process
We'll need your help to come up with a slogan/catch phrase and our easy 1,2,3 process so customers can see the poster and instantly have a clear understanding of what we do
1. Get an instant offer on our website
2. Send your item(s) to us
3.Get paid within 24 Hours
Industry/Entity Type
It Company
Look and feel
Each slider illustrates characteristics of the customer's brand and the style your logo design should communicate.

```html
<!DOCTYPE html>
<html lang="en">
<head>
<meta charset="utf-8">
<title>SwapHollow – Selling without the headache</title>
<link rel="stylesheet" href="https://fonts.googleapis.com/css2?family=Fredoka:wght@600&family=Roboto:wght@400&family=Roboto+Condensed:wght@400;700&display=swap">
<style>
  :root {
    --lime: #9ccb3b;
    --charcoal: #2f2b2a;
    --white: #ffffff;
    --ink: #231f20;
    --backdrop: #1c1c1c;
  }
  html, body {
    margin: 0;
    width: 1000px;
    height: 1200px;
    overflow: hidden;
    background: var(--backdrop);
  }
  h1, p { margin: 0; }
  .poster {
    position: absolute;
    left: 152px;
    top: 115px;
    width: 690px;
    height: 980px;
    overflow: hidden;
    background: var(--lime);
  }
  .poster-bg { position: absolute; inset: 0; }
  .mascot-art {
    position: absolute;
    left: 125px;
    top: 28px;
    width: 410px;
    height: 430px;
    border-radius: 48% 52% 40% 44%;
    background: radial-gradient(circle at 45% 35%, #f4c07a 0%, #b5d85c 45%, rgba(156,203,59,0) 72%);
  }
  .brand-name {
    position: absolute;
    top: 464px;
    left: 0;
    width: 100%;
    text-align: center;
    font: 600 76px/1 "Fredoka", sans-serif;
    color: var(--white);
    letter-spacing: -1px;
  }
  .slogan {
    position: absolute;
    top: 570px;
    left: 0;
    width: 100%;
    text-align: center;
    font: 400 41px/1 "Roboto", sans-serif;
    color: var(--white);
  }
  .slogan .accent { color: var(--lime); }
  .bubble {
    position: absolute;
    left: 196px;
    top: 631px;
    width: 298px;
    height: 42px;
    background: var(--white);
    border-radius: 8px;
    text-align: center;
    font: 400 29px/42px "Roboto", sans-serif;
    color: var(--ink);
  }
  .bubble::after {
    content: "";
    position: absolute;
    left: 136px;
    bottom: -16px;
    border: 11px solid transparent;
    border-top: 16px solid var(--white);
    border-bottom: 0;
  }
  .steps-art { position: absolute; inset: 0; pointer-events: none; }
  .step-number {
    position: absolute;
    width: 70px;
    height: 70px;
    margin-left: -39px;
    margin-top: -39px;
    border: 4px solid var(--white);
    border-radius: 50%;
    background: var(--lime);
    text-align: center;
    font: 700 58px/70px "Roboto Condensed", sans-serif;
    color: var(--ink);
  }
  .step-label {
    position: absolute;
    width: 200px;
    margin-left: -100px;
    top: 858px;
    text-align: center;
    font: 400 18px/22px "Roboto Condensed", sans-serif;
    color: var(--ink);
  }
  .step-label.middle { top: 854px; }
  .web-bar {
    position: absolute;
    left: 63px;
    top: 919px;
    width: 564px;
    height: 42px;
    border-radius: 6px;
    background: var(--lime);
    text-align: center;
    font: 700 35px/43px "Roboto Condensed", sans-serif;
    color: var(--ink);
  }
</style>
</head>
<body>
  <main class="poster">
    <svg class="poster-bg" viewBox="0 0 690 980" width="690" height="980" aria-hidden="true">
      <path d="M0,122 Q120,330 400,352 L400,368 Q130,350 0,190 Z" fill="var(--white)"/>
      <path d="M0,190 Q150,370 380,358 Q600,340 690,170 L690,980 L0,980 Z" fill="var(--charcoal)"/>
      <path d="M0,695 L345,752 L690,695 L690,980 L0,980 Z" fill="var(--white)"/>
    </svg>

    <div class="mascot-art" role="img" aria-label="Cartoon courier mascot in a green cap giving a thumbs up while running with an orange parcel"></div>

    <h1 class="brand-name">SwapHollow</h1>
    <p class="slogan">Selling without the <span class="accent">headache</span></p>
    <div class="bubble">It's simple</div>

    <svg class="steps-art" viewBox="0 0 690 980" width="690" height="980" aria-hidden="true">
      <line x1="248" y1="742" x2="248" y2="878" stroke="var(--ink)" stroke-width="1"/>
      <line x1="459" y1="742" x2="459" y2="878" stroke="var(--ink)" stroke-width="1"/>
      <polygon points="248,808 270,817 248,826" fill="var(--ink)"/>
      <polygon points="459,808 481,817 459,826" fill="var(--ink)"/>
      <rect x="111" y="795" width="56" height="35" rx="2" fill="none" stroke="var(--ink)" stroke-width="4"/>
      <path d="M100,834 H178 L174,841 H104 Z" fill="var(--ink)"/>
      <rect x="326" y="817" width="18" height="16" fill="var(--ink)"/>
      <rect x="346" y="808" width="14" height="25" fill="var(--ink)"/>
      <circle cx="335" cy="802" r="8" fill="none" stroke="var(--ink)" stroke-width="3"/>
      <path d="M364,796 V836 H322" fill="none" stroke="var(--ink)" stroke-width="3"/>
      <circle cx="328" cy="841" r="4" fill="var(--ink)"/>
      <circle cx="358" cy="841" r="4" fill="var(--ink)"/>
      <path d="M364,796 H372" stroke="var(--ink)" stroke-width="3"/>
      <path d="M570,800 L576,790 L582,795 L588,790 L594,800 Z" fill="var(--ink)"/>
      <path d="M572,804 H592 Q606,818 604,832 Q602,844 582,844 Q562,844 560,832 Q558,818 572,804 Z" fill="var(--ink)"/>
      <text x="582" y="834" text-anchor="middle" font-family="Roboto, sans-serif" font-size="22" fill="var(--white)">$</text>
    </svg>

    <div class="step-number" style="left:137px; top:717px;">1</div>
    <div class="step-number" style="left:346px; top:745px;">2</div>
    <div class="step-number" style="left:570px; top:717px;">3</div>

    <p class="step-label" style="left:137px;">Get an instant offer<br>on our website</p>
    <p class="step-label middle" style="left:348px;">Send your<br>item(s) to us</p>
    <p class="step-label" style="left:581px;">Get paid<br>within 24 Hours</p>

    <div class="web-bar">www.swaphollow.co.nz</div>
  </main>
</body>
</html>
```